REDESIGN SIGN UP PAGE - EASY TO READ AND UNDERSTAND QUICKLY

I need to redesign my sign up page DESKTOP AND MOBILE VERSION to include 2 products that are each available as a monthly subscription, 6 mth or 12 mth subscription.

Currently I only promote one product on my website but now will be two. https://www.brightlanepromoworks.biz/signup

Now I will have two products:

1. UNLIMITED VACATION CERTIFICATES, DINING VOUCHERS & SAVINGS INCENTIVES
Unlimited Monthly Plan $99 / Month + $199 One-Time Set-Up Fee
Unlimited Bi Annual Plan $490 / 6 Months + $199 One-Time Set-Up Fee
Unlimited Annual Plan $898 / 12 Months + $199 One-Time Set-Up Fee

2. UNLIMITED SMART DEVICE INCENTIVES & OTHER HARD PREMIUMS
Unlimited Monthly Plan $299 / Month + $199 One-Time Set-Up Fee
Unlimited Bi Annual Plan $1,590 / 6 Months + $199 One-Time Set-Up Fee
Unlimited Annual Plan $2,898 / 12 Months + $199 One-Time Set-Up Fee

When promoting the different plans you can see the different categories of incentives I offer here: https://www.brightlanepromoworks.biz/incentives

The SMART DEVICE CERTIFICATES & INCENTIVES category is for product #2 and all the rest of the Categories is for Product #1 Feel free to use images as a visual so customers can see that this product includes Vacations & Restaurants and this product includes only smart devices....

USE ALL CURRENT BULLET POINTS FOR BOTH PLANS THAT IS CURRENTLY ON WEBSITE. USE ALL CURRENT CONTENT ON WEBSITE ORIGINAL SIGN UP PAGE. DO NOT LEAVE ANY CONTENT OUT.

Target Market(s)

BUSINESS OWNERS

Industry/Entity Type

Marketing

Number of Pages Required

2 page

Requirements
Must have
• When promoting the 2 different products on the new sign up page you can see the different categories of incentives I offer here: https://www.brightlanepromoworks.biz/incentives fee; free to use images to showcase what each product offers.

The SMART DEVICE CERTIFICATES & INCENTIVES category is for product #2 and all the rest of the Categories is for Product #1

I want the user to easily understand we have two products that are available in 3 ways, monthly subscription, bi annual and annual and can see the price immediately for all 3 options for both products without toggling, etc.

Must be super clean easy to ready design. Not too busy at all please
Nice to have
• USE ALL CURRENT BULLET POINTS FOR BOTH PLANS THAT IS CURRENTLY ON WEBSITE. USE ALL CURRENT CONTENT ON WEBSITE ORIGINAL SIGN UP PAGE. DO NOT LEAVE ANY CONTENT OUT.

Should not have

```html
<!DOCTYPE html>
<html lang="en">
<head>
<meta charset="utf-8">
<title>Sign Up – Brightlane Promo Works</title>
<link href="https://fonts.googleapis.com/css2?family=Montserrat:wght@400;500;600;700&display=swap" rel="stylesheet">
<style>
:root{
  --blue:#1573c1;
  --blue-dark:#1168b3;
  --ink:#333;
  --muted:#5b5f66;
  --page:#f2f4f7;
  --price-bg:#e9eff5;
  --white:#fff;
  --green:#3bb54a;
  --green-dark:#1f9a45;
  --green-light:#7ef39a;
}
*{margin:0;padding:0;box-sizing:border-box}
html,body{width:1200px;height:3415px;overflow:hidden}
body{font-family:"Montserrat",sans-serif;color:var(--ink);background:var(--page);position:relative}
a{color:inherit;text-decoration:none}

.topbar{position:absolute;top:0;left:0;width:1200px;height:74px;background:var(--white);display:flex;align-items:center;justify-content:space-between;padding:0 46px 0 53px}
.brand{display:flex;align-items:center;gap:8px;font-weight:700;color:var(--blue);font-size:15px}
.brand-dot{width:14px;height:14px;border-radius:50%;background:var(--blue)}
.contact-line{font-size:12px;font-weight:600;color:#222;display:flex;gap:26px}

.navbar{position:absolute;top:74px;left:0;width:1200px;height:63px;background:var(--blue);display:flex;align-items:center;padding:0 59px;color:var(--white);font-size:12.5px;font-weight:600}
.navbar .links{display:flex;gap:26px}
.navbar .auth{margin-left:auto;display:flex;align-items:center;gap:29px}
.btn-login{background:var(--white);color:var(--blue);border-radius:18px;width:141px;height:34px;display:flex;align-items:center;justify-content:center}

.hero{position:absolute;top:137px;left:0;width:1200px;height:207px;background:var(--blue);color:var(--white);text-align:center;padding-top:66px}
.hero h1{font-size:21.5px;font-weight:700;line-height:26px;letter-spacing:.2px}
.hero p{font-size:12.5px;font-weight:400;color:#bcd8f1;line-height:17px;margin-top:6px}

.tabs{position:absolute;top:344px;left:0;width:1200px;height:54px;background:var(--white);box-shadow:0 1px 3px rgba(0,0,0,.08)}
.tab{position:absolute;top:21px;font-size:14.5px;font-weight:700;color:#1d3552}
.tab.active{color:var(--blue)}
.tab-underline{position:absolute;left:469px;top:50px;width:137px;height:3px;background:var(--blue)}

.plan-intro{position:absolute;left:0;width:1200px;text-align:center;color:var(--muted);font-size:15px;line-height:19px;text-transform:uppercase}
.plan-intro strong{display:block;color:#1d2a3a;font-weight:700;font-size:15px;margin-bottom:18px}

.cards{position:absolute;left:94px;width:1033px;display:flex;gap:26px}
.card{width:327px;height:1154px;background:var(--white);box-shadow:0 2px 6px rgba(0,0,0,.12);display:flex;flex-direction:column}
.card-head{height:112px;text-align:center;padding-top:25px}
.card-head h2{font-size:18px;font-weight:700;color:var(--blue)}
.card-head p{font-size:12px;font-weight:600;color:#222;line-height:15px;margin-top:12px}
.price{height:200px;background:var(--price-bg);padding:28px 32px 0}
.price-row{display:flex;align-items:center;justify-content:space-between;height:76px}
.amount{text-align:center;color:var(--blue);font-weight:700;font-size:44px;line-height:44px}
.amount span{display:block;color:#1d1d1d;font-size:17px;line-height:22px;margin-top:4px}
.plus{font-size:30px;font-weight:500;color:#222}
.fee{font-size:21px;font-weight:700;color:#111;line-height:24px}
.fee span{display:block;font-size:11px;font-weight:400;line-height:14px}
.btn-select{display:flex;align-items:center;justify-content:center;height:44px;border-radius:22px;background:var(--blue);color:var(--white);font-weight:700;font-size:16px;letter-spacing:.6px;margin-top:18px}
.types{height:50px;border-bottom:1px solid #e6e9ee;text-align:center;font-size:19px;font-weight:600;color:#444;line-height:50px}
.features{list-style:none;padding:26px 28px 0 48px}
.features li{position:relative;font-size:12.3px;line-height:15px;color:var(--muted);margin-bottom:15px;padding-left:0}
.features li svg{position:absolute;left:-22px;top:3px}
.btn-outline{margin:auto 28px 24px 26px;height:45px;border:1.5px solid var(--blue);border-radius:23px;color:var(--blue);font-weight:700;font-size:16px;letter-spacing:.6px;display:flex;align-items:center;justify-content:center}

.footer{position:absolute;top:3013px;left:0;width:1200px;height:402px;background:var(--blue);color:var(--white)}
.socials{position:absolute;left:120px;top:20px;display:flex;gap:30px}
.socials span{width:22px;height:22px;border-radius:50%;background:var(--white);opacity:.95}
.footer-brand{position:absolute;left:94px;top:61px;width:248px;height:73px;background:var(--white);border-radius:0 0 14px 14px;display:flex;align-items:center;justify-content:center}
.samples{position:absolute;left:84px;top:212px;width:327px;height:90px}
.samples svg{position:absolute;left:0;top:0}
.samples-text{position:absolute;left:0;top:24px;width:300px;text-align:center;font-weight:700}
.samples-text b{display:block;font-size:20px;letter-spacing:.5px}
.samples-text i{display:block;font-style:normal;color:var(--green-light);font-size:18px;margin-top:4px}
.f-col{position:absolute;top:25px}
.f-col h3{font-size:16px;font-weight:700;letter-spacing:.3px;margin-bottom:25px}
.f-col ul{list-style:none}
.f-col li{font-size:11.5px;line-height:14px;margin-bottom:16px}
.contact{left:513px;width:270px}
.contact li{position:relative;padding-left:19px;margin-bottom:12px}
.contact li svg{position:absolute;left:0;top:2px}
</style>
</head>
<body>

<header class="topbar">
  <div class="brand"><span class="brand-dot"></span>Brightlane Promo Works</div>
  <div class="contact-line"><span>CALL US: 1-555-301-4420</span><span>TEXT US: 1-555-302-0</span></div>
</header>

<nav class="navbar">
  <div class="links"><a>Home</a><a>The Incentives</a><a>Samples</a><a>Industries</a><a>Testimonials</a><a>Faq</a></div>
  <div class="auth"><a class="btn-login">Login</a><a>Signup</a></div>
</nav>

<section class="hero">
  <h1>CONGRATULATIONS ON MAKING THE DECISION<br>TO MAKE MORE MONEY FOR YOUR BUSINESS</h1>
  <p>This program is an online subscription based incentive<br>marketing system with the following features</p>
</section>

<div class="tabs">
  <span class="tab active" style="left:505px">PLANE 1</span>
  <span class="tab" style="left:667px">PLANE 2</span>
  <span class="tab-underline"></span>
</div>

<div class="plan-intro" style="top:437px">Unlimited Vacation Certificates, Dining<br>Vouchers &amp; Savings Incentives</div>

<!-- Plane 1 cards -->
<div class="cards" style="top:517px">
  <article class="card">
    <div class="card-head"><h2>UNLIMITED MONTHLY PLAN</h2><p>One Account Can Be Used<br>For Unlimited Brands</p></div>
    <div class="price">
      <div class="price-row"><div class="amount">$99<span>Month</span></div><div class="plus">+</div><div class="fee">$199<span>One-time<br>Set-up fee</span></div></div>
      <a class="btn-select">SELECT</a>
    </div>
    <div class="types">Unlimited Certificate Types</div>
    <ul class="features" style="padding-right:50px">
      <li><svg width="12" height="10" viewBox="0 0 12 10"><path d="M1 5l3.5 3.5L11 1" fill="none" stroke="#3bb54a" stroke-width="2"/></svg>Unlimited E-Certificates</li>
      <li><svg width="12" height="10" viewBox="0 0 12 10"><path d="M1 5l3.5 3.5L11 1" fill="none" stroke="#3bb54a" stroke-width="2"/></svg>Unlimited SMS Certificates</li>
      <li><svg width="12" height="10" viewBox="0 0 12 10"><path d="M1 5l3.5 3.5L11 1" fill="none" stroke="#3bb54a" stroke-width="2"/></svg>Unlimited Web Banner Certificates</li>
      <li><svg width="12" height="10" viewBox="0 0 12 10"><path d="M1 5l3.5 3.5L11 1" fill="none" stroke="#3bb54a" stroke-width="2"/></svg>Unlimited White Label Certificate Landing Pages</li>
      <li><svg width="12" height="10" viewBox="0 0 12 10"><path d="M1 5l3.5 3.5L11 1" fill="none" stroke="#3bb54a" stroke-width="2"/></svg>Unlimited Website Sticky Bar Certificates</li>
      <li><svg width="12" height="10" viewBox="0 0 12 10"><path d="M1 5l3.5 3.5L11 1" fill="none" stroke="#3bb54a" stroke-width="2"/></svg>Unlimited Website Pop Up Certificate</li>
      <li><svg width="12" height="10" viewBox="0 0 12 10"><path d="M1 5l3.5 3.5L11 1" fill="none" stroke="#3bb54a" stroke-width="2"/></svg>Unlimited API E-Certificates</li>
      <li><svg width="12" height="10" viewBox="0 0 12 10"><path d="M1 5l3.5 3.5L11 1" fill="none" stroke="#3bb54a" stroke-width="2"/></svg>Unlimited Autoflow Integration Access</li>
      <li><svg width="12" height="10" viewBox="0 0 12 10"><path d="M1 5l3.5 3.5L11 1" fill="none" stroke="#3bb54a" stroke-width="2"/></svg>FREE Warm Lead Letter Templates</li>
      <li><svg width="12" height="10" viewBox="0 0 12 10"><path d="M1 5l3.5 3.5L11 1" fill="none" stroke="#3bb54a" stroke-width="2"/></svg>FREE Customer Appreciation Letter Templates</li>
      <li><svg width="12" height="10" viewBox="0 0 12 10"><path d="M1 5l3.5 3.5L11 1" fill="none" stroke="#3bb54a" stroke-width="2"/></svg>FREE Professional-Grade Incentive Videos</li>
      <li><svg width="12" height="10" viewBox="0 0 12 10"><path d="M1 5l3.5 3.5L11 1" fill="none" stroke="#3bb54a" stroke-width="2"/></svg>FREE Proven Social Ad Templates</li>
      <li><svg width="12" height="10" viewBox="0 0 12 10"><path d="M1 5l3.5 3.5L11 1" fill="none" stroke="#3bb54a" stroke-width="2"/></svg>FREE High-Converting Banner Ad Templates</li>
      <li><svg width="12" height="10" viewBox="0 0 12 10"><path d="M1 5l3.5 3.5L11 1" fill="none" stroke="#3bb54a" stroke-width="2"/></svg>FREE Time-Tested Print Ad Templates</li>
      <li><svg width="12" height="10" viewBox="0 0 12 10"><path d="M1 5l3.5 3.5L11 1" fill="none" stroke="#3bb54a" stroke-width="2"/></svg>FREE White Label Redemption Website</li>
      <li><svg width="12" height="10" viewBox="0 0 12 10"><path d="M1 5l3.5 3.5L11 1" fill="none" stroke="#3bb54a" stroke-width="2"/></svg>FREE Industry Specific Ad Packs</li>
      <li><svg width="12" height="10" viewBox="0 0 12 10"><path d="M1 5l3.5 3.5L11 1" fill="none" stroke="#3bb54a" stroke-width="2"/></svg>FREE Affiliate Program-Earn 50% Commissions</li>
      <li><svg width="12" height="10" viewBox="0 0 12 10"><path d="M1 5l3.5 3.5L11 1" fill="none" stroke="#3bb54a" stroke-width="2"/></svg>FREE Eye-Catching Posters, Flyers &amp; Brochures Each Certificate</li>
      <li><svg width="12" height="10" viewBox="0 0 12 10"><path d="M1 5l3.5 3.5L11 1" fill="none" stroke="#3bb54a" stroke-width="2"/></svg>FREE Step by Step Redemption Guides</li>
    </ul>
    <a class="btn-outline">SELECT</a>
  </article>

  <article class="card">
    <div class="card-head"><h2>UNLIMITED BI ANNUAL PLAN</h2><p>One Account Can Be Used<br>For Unlimited Brands</p></div>
    <div class="price">
      <div class="price-row"><div class="amount">$490<span>6 Months</span></div><div class="plus">+</div><div class="fee">$199<span>One-time<br>Set-up fee</span></div></div>
      <a class="btn-select">SELECT</a>
    </div>
    <div class="types">Unlimited Certificate Types</div>
    <ul class="features">
      <li><svg width="12" height="10" viewBox="0 0 12 10"><path d="M1 5l3.5 3.5L11 1" fill="none" stroke="#3bb54a" stroke-width="2"/></svg>Unlimited E-Certificates</li>
      <li><svg width="12" height="10" viewBox="0 0 12 10"><path d="M1 5l3.5 3.5L11 1" fill="none" stroke="#3bb54a" stroke-width="2"/></svg>Unlimited SMS Certificates</li>
      <li><svg width="12" height="10" viewBox="0 0 12 10"><path d="M1 5l3.5 3.5L11 1" fill="none" stroke="#3bb54a" stroke-width="2"/></svg>Unlimited Web Banner Certificates</li>
      <li><svg width="12" height="10" viewBox="0 0 12 10"><path d="M1 5l3.5 3.5L11 1" fill="none" stroke="#3bb54a" stroke-width="2"/></svg>Unlimited White Label Certificate<br>Landing Pages</li>
      <li><svg width="12" height="10" viewBox="0 0 12 10"><path d="M1 5l3.5 3.5L11 1" fill="none" stroke="#3bb54a" stroke-width="2"/></svg>Unlimited Website Sticky Bar<br>Certificates</li>
      <li><svg width="12" height="10" viewBox="0 0 12 10"><path d="M1 5l3.5 3.5L11 1" fill="none" stroke="#3bb54a" stroke-width="2"/></svg>Unlimited Website Pop Up Certificate</li>
      <li><svg width="12" height="10" viewBox="0 0 12 10"><path d="M1 5l3.5 3.5L11 1" fill="none" stroke="#3bb54a" stroke-width="2"/></svg>Unlimited API E-Certificates</li>
      <li><svg width="12" height="10" viewBox="0 0 12 10"><path d="M1 5l3.5 3.5L11 1" fill="none" stroke="#3bb54a" stroke-width="2"/></svg>Unlimited Autoflow Integration Access</li>
      <li><svg width="12" height="10" viewBox="0 0 12 10"><path d="M1 5l3.5 3.5L11 1" fill="none" stroke="#3bb54a" stroke-width="2"/></svg>FREE Warm Lead Letter Templates</li>
      <li><svg width="12" height="10" viewBox="0 0 12 10"><path d="M1 5l3.5 3.5L11 1" fill="none" stroke="#3bb54a" stroke-width="2"/></svg>FREE Customer Appreciation Letter<br>Templates</li>
      <li><svg width="12" height="10" viewBox="0 0 12 10"><path d="M1 5l3.5 3.5L11 1" fill="none" stroke="#3bb54a" stroke-width="2"/></svg>FREE Professional-Grade Incentive<br>Videos</li>
      <li><svg width="12" height="10" viewBox="0 0 12 10"><path d="M1 5l3.5 3.5L11 1" fill="none" stroke="#3bb54a" stroke-width="2"/></svg>FREE Proven Social Ad Templates</li>
      <li><svg width="12" height="10" viewBox="0 0 12 10"><path d="M1 5l3.5 3.5L11 1" fill="none" stroke="#3bb54a" stroke-width="2"/></svg>FREE High-Converting Banner Ad<br>Templates</li>
      <li><svg width="12" height="10" viewBox="0 0 12 10"><path d="M1 5l3.5 3.5L11 1" fill="none" stroke="#3bb54a" stroke-width="2"/></svg>FREE Time-Tested Print Ad Templates</li>
      <li><svg width="12" height="10" viewBox="0 0 12 10"><path d="M1 5l3.5 3.5L11 1" fill="none" stroke="#3bb54a" stroke-width="2"/></svg>FREE White Label Redemption Website</li>
      <li><svg width="12" height="10" viewBox="0 0 12 10"><path d="M1 5l3.5 3.5L11 1" fill="none" stroke="#3bb54a" stroke-width="2"/></svg>FREE Industry Specific Ad Packs</li>
      <li><svg width="12" height="10" viewBox="0 0 12 10"><path d="M1 5l3.5 3.5L11 1" fill="none" stroke="#3bb54a" stroke-width="2"/></svg>FREE Affiliate Program-Earn 50%<br>Commissions</li>
      <li><svg width="12" height="10" viewBox="0 0 12 10"><path d="M1 5l3.5 3.5L11 1" fill="none" stroke="#3bb54a" stroke-width="2"/></svg>FREE Eye-Catching Posters, Flyers &amp;<br>Brochures Each Certificate</li>
      <li><svg width="12" height="10" viewBox="0 0 12 10"><path d="M1 5l3.5 3.5L11 1" fill="none" stroke="#3bb54a" stroke-width="2"/></svg>FREE Step by Step Redemption Guides</li>
    </ul>
    <a class="btn-outline">SELECT</a>
  </article>

  <article class="card">
    <div class="card-head"><h2>UNLIMITED ANNUAL PLAN</h2><p>One Account Can Be Used<br>For Unlimited Brands</p></div>
    <div class="price">
      <div class="price-row"><div class="amount">$898<span>12 Months</span></div><div class="plus">+</div><div class="fee">$199<span>One-time<br>Set-up fee</span></div></div>
      <a class="btn-select">SELECT</a>
    </div>
    <div class="types">Unlimited Certificate Types</div>
    <ul class="features">
      <li><svg width="12" height="10" viewBox="0 0 12 10"><path d="M1 5l3.5 3.5L11 1" fill="none" stroke="#3bb54a" stroke-width="2"/></svg>Unlimited E-Certificates</li>
      <li><svg width="12" height="10" viewBox="0 0 12 10"><path d="M1 5l3.5 3.5L11 1" fill="none" stroke="#3bb54a" stroke-width="2"/></svg>Unlimited SMS Certificates</li>
      <li><svg width="12" height="10" viewBox="0 0 12 10"><path d="M1 5l3.5 3.5L11 1" fill="none" stroke="#3bb54a" stroke-width="2"/></svg>Unlimited Web Banner Certificates</li>
      <li><svg width="12" height="10" viewBox="0 0 12 10"><path d="M1 5l3.5 3.5L11 1" fill="none" stroke="#3bb54a" stroke-width="2"/></svg>Unlimited White Label Certificate<br>Landing Pages</li>
      <li><svg width="12" height="10" viewBox="0 0 12 10"><path d="M1 5l3.5 3.5L11 1" fill="none" stroke="#3bb54a" stroke-width="2"/></svg>Unlimited Website Sticky Bar<br>Certificates</li>
      <li><svg width="12" height="10" viewBox="0 0 12 10"><path d="M1 5l3.5 3.5L11 1" fill="none" stroke="#3bb54a" stroke-width="2"/></svg>Unlimited Website Pop Up Certificate</li>
      <li><svg width="12" height="10" viewBox="0 0 12 10"><path d="M1 5l3.5 3.5L11 1" fill="none" stroke="#3bb54a" stroke-width="2"/></svg>Unlimited API E-Certificates</li>
      <li><svg width="12" height="10" viewBox="0 0 12 10"><path d="M1 5l3.5 3.5L11 1" fill="none" stroke="#3bb54a" stroke-width="2"/></svg>Unlimited Autoflow Integration Access</li>
      <li><svg width="12" height="10" viewBox="0 0 12 10"><path d="M1 5l3.5 3.5L11 1" fill="none" stroke="#3bb54a" stroke-width="2"/></svg>FREE Warm Lead Letter Templates</li>
      <li><svg width="12" height="10" viewBox="0 0 12 10"><path d="M1 5l3.5 3.5L11 1" fill="none" stroke="#3bb54a" stroke-width="2"/></svg>FREE Customer Appreciation Letter<br>Templates</li>
      <li><svg width="12" height="10" viewBox="0 0 12 10"><path d="M1 5l3.5 3.5L11 1" fill="none" stroke="#3bb54a" stroke-width="2"/></svg>FREE Professional-Grade Incentive<br>Videos</li>
      <li><svg width="12" height="10" viewBox="0 0 12 10"><path d="M1 5l3.5 3.5L11 1" fill="none" stroke="#3bb54a" stroke-width="2"/></svg>FREE Proven Social Ad Templates</li>
      <li><svg width="12" height="10" viewBox="0 0 12 10"><path d="M1 5l3.5 3.5L11 1" fill="none" stroke="#3bb54a" stroke-width="2"/></svg>FREE High-Converting Banner Ad<br>Templates</li>
      <li><svg width="12" height="10" viewBox="0 0 12 10"><path d="M1 5l3.5 3.5L11 1" fill="none" stroke="#3bb54a" stroke-width="2"/></svg>FREE Time-Tested Print Ad Templates</li>
      <li><svg width="12" height="10" viewBox="0 0 12 10"><path d="M1 5l3.5 3.5L11 1" fill="none" stroke="#3bb54a" stroke-width="2"/></svg>FREE White Label Redemption Website</li>
      <li><svg width="12" height="10" viewBox="0 0 12 10"><path d="M1 5l3.5 3.5L11 1" fill="none" stroke="#3bb54a" stroke-width="2"/></svg>FREE Industry Specific Ad Packs</li>
      <li><svg width="12" height="10" viewBox="0 0 12 10"><path d="M1 5l3.5 3.5L11 1" fill="none" stroke="#3bb54a" stroke-width="2"/></svg>FREE Affiliate Program-Earn 50%<br>Commissions</li>
      <li><svg width="12" height="10" viewBox="0 0 12 10"><path d="M1 5l3.5 3.5L11 1" fill="none" stroke="#3bb54a" stroke-width="2"/></svg>FREE Eye-Catching Posters, Flyers &amp;<br>Brochures Each Certificate</li>
      <li><svg width="12" height="10" viewBox="0 0 12 10"><path d="M1 5l3.5 3.5L11 1" fill="none" stroke="#3bb54a" stroke-width="2"/></svg>FREE Step by Step Redemption Guides</li>
    </ul>
    <a class="btn-outline">SELECT</a>
  </article>
</div>

<div class="plan-intro" style="top:1724px"><strong>PLANE 2</strong>Unlimited Smart Device Incentives &amp; Other Hard Premiums</div>

<!-- Plane 2 cards -->
<div class="cards" style="top:1817px">
  <article class="card">
    <div class="card-head"><h2>UNLIMITED MONTHLY PLAN</h2><p>One Account Can Be Used<br>For Unlimited Brands</p></div>
    <div class="price">
      <div class="price-row"><div class="amount">$299<span>Month</span></div><div class="plus">+</div><div class="fee">$199<span>One-time<br>Set-up fee</span></div></div>
      <a class="btn-select">SELECT</a>
    </div>
    <div class="types">Unlimited Certificate Types</div>
    <ul class="features" style="padding-right:50px">
      <li><svg width="12" height="10" viewBox="0 0 12 10"><path d="M1 5l3.5 3.5L11 1" fill="none" stroke="#3bb54a" stroke-width="2"/></svg>Unlimited E-Certificates</li>
      <li><svg width="12" height="10" viewBox="0 0 12 10"><path d="M1 5l3.5 3.5L11 1" fill="none" stroke="#3bb54a" stroke-width="2"/></svg>Unlimited SMS Certificates</li>
      <li><svg width="12" height="10" viewBox="0 0 12 10"><path d="M1 5l3.5 3.5L11 1" fill="none" stroke="#3bb54a" stroke-width="2"/></svg>Unlimited Web Banner Certificates</li>
      <li><svg width="12" height="10" viewBox="0 0 12 10"><path d="M1 5l3.5 3.5L11 1" fill="none" stroke="#3bb54a" stroke-width="2"/></svg>Unlimited White Label Certificate Landing Pages</li>
      <li><svg width="12" height="10" viewBox="0 0 12 10"><path d="M1 5l3.5 3.5L11 1" fill="none" stroke="#3bb54a" stroke-width="2"/></svg>Unlimited Website Sticky Bar Certificates</li>
      <li><svg width="12" height="10" viewBox="0 0 12 10"><path d="M1 5l3.5 3.5L11 1" fill="none" stroke="#3bb54a" stroke-width="2"/></svg>Unlimited Website Pop Up Certificate</li>
      <li><svg width="12" height="10" viewBox="0 0 12 10"><path d="M1 5l3.5 3.5L11 1" fill="none" stroke="#3bb54a" stroke-width="2"/></svg>Unlimited API E-Certificates</li>
      <li><svg width="12" height="10" viewBox="0 0 12 10"><path d="M1 5l3.5 3.5L11 1" fill="none" stroke="#3bb54a" stroke-width="2"/></svg>Unlimited Autoflow Integration Access</li>
      <li><svg width="12" height="10" viewBox="0 0 12 10"><path d="M1 5l3.5 3.5L11 1" fill="none" stroke="#3bb54a" stroke-width="2"/></svg>FREE Warm Lead Letter Templates</li>
      <li><svg width="12" height="10" viewBox="0 0 12 10"><path d="M1 5l3.5 3.5L11 1" fill="none" stroke="#3bb54a" stroke-width="2"/></svg>FREE Customer Appreciation Letter Templates</li>
      <li><svg width="12" height="10" viewBox="0 0 12 10"><path d="M1 5l3.5 3.5L11 1" fill="none" stroke="#3bb54a" stroke-width="2"/></svg>FREE Professional-Grade Incentive Videos</li>
      <li><svg width="12" height="10" viewBox="0 0 12 10"><path d="M1 5l3.5 3.5L11 1" fill="none" stroke="#3bb54a" stroke-width="2"/></svg>FREE Proven Social Ad Templates</li>
      <li><svg width="12" height="10" viewBox="0 0 12 10"><path d="M1 5l3.5 3.5L11 1" fill="none" stroke="#3bb54a" stroke-width="2"/></svg>FREE High-Converting Banner Ad Templates</li>
      <li><svg width="12" height="10" viewBox="0 0 12 10"><path d="M1 5l3.5 3.5L11 1" fill="none" stroke="#3bb54a" stroke-width="2"/></svg>FREE Time-Tested Print Ad Templates</li>
      <li><svg width="12" height="10" viewBox="0 0 12 10"><path d="M1 5l3.5 3.5L11 1" fill="none" stroke="#3bb54a" stroke-width="2"/></svg>FREE White Label Redemption Website</li>
      <li><svg width="12" height="10" viewBox="0 0 12 10"><path d="M1 5l3.5 3.5L11 1" fill="none" stroke="#3bb54a" stroke-width="2"/></svg>FREE Industry Specific Ad Packs</li>
      <li><svg width="12" height="10" viewBox="0 0 12 10"><path d="M1 5l3.5 3.5L11 1" fill="none" stroke="#3bb54a" stroke-width="2"/></svg>FREE Affiliate Program-Earn 50% Commissions</li>
      <li><svg width="12" height="10" viewBox="0 0 12 10"><path d="M1 5l3.5 3.5L11 1" fill="none" stroke="#3bb54a" stroke-width="2"/></svg>FREE Eye-Catching Posters, Flyers &amp; Brochures Each Certificate</li>
      <li><svg width="12" height="10" viewBox="0 0 12 10"><path d="M1 5l3.5 3.5L11 1" fill="none" stroke="#3bb54a" stroke-width="2"/></svg>FREE Step by Step Redemption Guides</li>
    </ul>
    <a class="btn-outline">SELECT</a>
  </article>

  <article class="card">
    <div class="card-head"><h2>UNLIMITED BI ANNUAL PLAN</h2><p>One Account Can Be Used<br>For Unlimited Brands</p></div>
    <div class="price">
      <div class="price-row"><div class="amount">$1,590<span>6 Months</span></div><div class="plus">+</div><div class="fee">$199<span>One-time<br>Set-up fee</span></div></div>
      <a class="btn-select">SELECT</a>
    </div>
    <div class="types">Unlimited Certificate Types</div>
    <ul class="features">
      <li><svg width="12" height="10" viewBox="0 0 12 10"><path d="M1 5l3.5 3.5L11 1" fill="none" stroke="#3bb54a" stroke-width="2"/></svg>Unlimited E-Certificates</li>
      <li><svg width="12" height="10" viewBox="0 0 12 10"><path d="M1 5l3.5 3.5L11 1" fill="none" stroke="#3bb54a" stroke-width="2"/></svg>Unlimited SMS Certificates</li>
      <li><svg width="12" height="10" viewBox="0 0 12 10"><path d="M1 5l3.5 3.5L11 1" fill="none" stroke="#3bb54a" stroke-width="2"/></svg>Unlimited Web Banner Certificates</li>
      <li><svg width="12" height="10" viewBox="0 0 12 10"><path d="M1 5l3.5 3.5L11 1" fill="none" stroke="#3bb54a" stroke-width="2"/></svg>Unlimited White Label Certificate<br>Landing Pages</li>
      <li><svg width="12" height="10" viewBox="0 0 12 10"><path d="M1 5l3.5 3.5L11 1" fill="none" stroke="#3bb54a" stroke-width="2"/></svg>Unlimited Website Sticky Bar<br>Certificates</li>
      <li><svg width="12" height="10" viewBox="0 0 12 10"><path d="M1 5l3.5 3.5L11 1" fill="none" stroke="#3bb54a" stroke-width="2"/></svg>Unlimited Website Pop Up Certificate</li>
      <li><svg width="12" height="10" viewBox="0 0 12 10"><path d="M1 5l3.5 3.5L11 1" fill="none" stroke="#3bb54a" stroke-width="2"/></svg>Unlimited API E-Certificates</li>
      <li><svg width="12" height="10" viewBox="0 0 12 10"><path d="M1 5l3.5 3.5L11 1" fill="none" stroke="#3bb54a" stroke-width="2"/></svg>Unlimited Autoflow Integration Access</li>
      <li><svg width="12" height="10" viewBox="0 0 12 10"><path d="M1 5l3.5 3.5L11 1" fill="none" stroke="#3bb54a" stroke-width="2"/></svg>FREE Warm Lead Letter Templates</li>
      <li><svg width="12" height="10" viewBox="0 0 12 10"><path d="M1 5l3.5 3.5L11 1" fill="none" stroke="#3bb54a" stroke-width="2"/></svg>FREE Customer Appreciation Letter<br>Templates</li>
      <li><svg width="12" height="10" viewBox="0 0 12 10"><path d="M1 5l3.5 3.5L11 1" fill="none" stroke="#3bb54a" stroke-width="2"/></svg>FREE Professional-Grade Incentive<br>Videos</li>
      <li><svg width="12" height="10" viewBox="0 0 12 10"><path d="M1 5l3.5 3.5L11 1" fill="none" stroke="#3bb54a" stroke-width="2"/></svg>FREE Proven Social Ad Templates</li>
      <li><svg width="12" height="10" viewBox="0 0 12 10"><path d="M1 5l3.5 3.5L11 1" fill="none" stroke="#3bb54a" stroke-width="2"/></svg>FREE High-Converting Banner Ad<br>Templates</li>
      <li><svg width="12" height="10" viewBox="0 0 12 10"><path d="M1 5l3.5 3.5L11 1" fill="none" stroke="#3bb54a" stroke-width="2"/></svg>FREE Time-Tested Print Ad Templates</li>
      <li><svg width="12" height="10" viewBox="0 0 12 10"><path d="M1 5l3.5 3.5L11 1" fill="none" stroke="#3bb54a" stroke-width="2"/></svg>FREE White Label Redemption Website</li>
      <li><svg width="12" height="10" viewBox="0 0 12 10"><path d="M1 5l3.5 3.5L11 1" fill="none" stroke="#3bb54a" stroke-width="2"/></svg>FREE Industry Specific Ad Packs</li>
      <li><svg width="12" height="10" viewBox="0 0 12 10"><path d="M1 5l3.5 3.5L11 1" fill="none" stroke="#3bb54a" stroke-width="2"/></svg>FREE Affiliate Program-Earn 50%<br>Commissions</li>
      <li><svg width="12" height="10" viewBox="0 0 12 10"><path d="M1 5l3.5 3.5L11 1" fill="none" stroke="#3bb54a" stroke-width="2"/></svg>FREE Eye-Catching Posters, Flyers &amp;<br>Brochures Each Certificate</li>
      <li><svg width="12" height="10" viewBox="0 0 12 10"><path d="M1 5l3.5 3.5L11 1" fill="none" stroke="#3bb54a" stroke-width="2"/></svg>FREE Step by Step Redemption Guides</li>
    </ul>
    <a class="btn-outline">SELECT</a>
  </article>

  <article class="card">
    <div class="card-head"><h2>UNLIMITED ANNUAL PLAN</h2><p>One Account Can Be Used<br>For Unlimited Brands</p></div>
    <div class="price">
      <div class="price-row"><div class="amount">$2,898<span>12 Months</span></div><div class="plus">+</div><div class="fee">$199<span>One-time<br>Set-up fee</span></div></div>
      <a class="btn-select">SELECT</a>
    </div>
    <div class="types">Unlimited Certificate Types</div>
    <ul class="features">
      <li><svg width="12" height="10" viewBox="0 0 12 10"><path d="M1 5l3.5 3.5L11 1" fill="none" stroke="#3bb54a" stroke-width="2"/></svg>Unlimited E-Certificates</li>
      <li><svg width="12" height="10" viewBox="0 0 12 10"><path d="M1 5l3.5 3.5L11 1" fill="none" stroke="#3bb54a" stroke-width="2"/></svg>Unlimited SMS Certificates</li>
      <li><svg width="12" height="10" viewBox="0 0 12 10"><path d="M1 5l3.5 3.5L11 1" fill="none" stroke="#3bb54a" stroke-width="2"/></svg>Unlimited Web Banner Certificates</li>
      <li><svg width="12" height="10" viewBox="0 0 12 10"><path d="M1 5l3.5 3.5L11 1" fill="none" stroke="#3bb54a" stroke-width="2"/></svg>Unlimited White Label Certificate<br>Landing Pages</li>
      <li><svg width="12" height="10" viewBox="0 0 12 10"><path d="M1 5l3.5 3.5L11 1" fill="none" stroke="#3bb54a" stroke-width="2"/></svg>Unlimited Website Sticky Bar<br>Certificates</li>
      <li><svg width="12" height="10" viewBox="0 0 12 10"><path d="M1 5l3.5 3.5L11 1" fill="none" stroke="#3bb54a" stroke-width="2"/></svg>Unlimited Website Pop Up Certificate</li>
      <li><svg width="12" height="10" viewBox="0 0 12 10"><path d="M1 5l3.5 3.5L11 1" fill="none" stroke="#3bb54a" stroke-width="2"/></svg>Unlimited API E-Certificates</li>
      <li><svg width="12" height="10" viewBox="0 0 12 10"><path d="M1 5l3.5 3.5L11 1" fill="none" stroke="#3bb54a" stroke-width="2"/></svg>Unlimited Autoflow Integration Access</li>
      <li><svg width="12" height="10" viewBox="0 0 12 10"><path d="M1 5l3.5 3.5L11 1" fill="none" stroke="#3bb54a" stroke-width="2"/></svg>FREE Warm Lead Letter Templates</li>
      <li><svg width="12" height="10" viewBox="0 0 12 10"><path d="M1 5l3.5 3.5L11 1" fill="none" stroke="#3bb54a" stroke-width="2"/></svg>FREE Customer Appreciation Letter<br>Templates</li>
      <li><svg width="12" height="10" viewBox="0 0 12 10"><path d="M1 5l3.5 3.5L11 1" fill="none" stroke="#3bb54a" stroke-width="2"/></svg>FREE Professional-Grade Incentive<br>Videos</li>
      <li><svg width="12" height="10" viewBox="0 0 12 10"><path d="M1 5l3.5 3.5L11 1" fill="none" stroke="#3bb54a" stroke-width="2"/></svg>FREE Proven Social Ad Templates</li>
      <li><svg width="12" height="10" viewBox="0 0 12 10"><path d="M1 5l3.5 3.5L11 1" fill="none" stroke="#3bb54a" stroke-width="2"/></svg>FREE High-Converting Banner Ad<br>Templates</li>
      <li><svg width="12" height="10" viewBox="0 0 12 10"><path d="M1 5l3.5 3.5L11 1" fill="none" stroke="#3bb54a" stroke-width="2"/></svg>FREE Time-Tested Print Ad Templates</li>
      <li><svg width="12" height="10" viewBox="0 0 12 10"><path d="M1 5l3.5 3.5L11 1" fill="none" stroke="#3bb54a" stroke-width="2"/></svg>FREE White Label Redemption Website</li>
      <li><svg width="12" height="10" viewBox="0 0 12 10"><path d="M1 5l3.5 3.5L11 1" fill="none" stroke="#3bb54a" stroke-width="2"/></svg>FREE Industry Specific Ad Packs</li>
      <li><svg width="12" height="10" viewBox="0 0 12 10"><path d="M1 5l3.5 3.5L11 1" fill="none" stroke="#3bb54a" stroke-width="2"/></svg>FREE Affiliate Program-Earn 50%<br>Commissions</li>
      <li><svg width="12" height="10" viewBox="0 0 12 10"><path d="M1 5l3.5 3.5L11 1" fill="none" stroke="#3bb54a" stroke-width="2"/></svg>FREE Eye-Catching Posters, Flyers &amp;<br>Brochures Each Certificate</li>
      <li><svg width="12" height="10" viewBox="0 0 12 10"><path d="M1 5l3.5 3.5L11 1" fill="none" stroke="#3bb54a" stroke-width="2"/></svg>FREE Step by Step Redemption Guides</li>
    </ul>
    <a class="btn-outline">SELECT</a>
  </article>
</div>

<footer class="footer">
  <div class="socials" aria-label="Social links"><span></span><span></span><span></span><span></span></div>
  <div class="footer-brand"><div class="brand"><span class="brand-dot"></span>Brightlane Promo Works</div></div>

  <div class="samples">
    <svg width="327" height="90" viewBox="0 0 327 90">
      <polygon points="0,0 295,0 327,45 295,90 0,90 18,45" fill="var(--green-dark)"/>
      <polygon points="6,4 290,4 320,45 290,86 6,86 22,45" fill="var(--green)"/>
    </svg>
    <div class="samples-text"><b>GET FREE SAMPLES</b><i>100% FREE</i></div>
  </div>

  <div class="f-col contact">
    <h3>CONTACT US</h3>
    <ul>
      <li><svg width="12" height="14" viewBox="0 0 12 14"><path d="M6 13s5-5 5-8a5 5 0 0 0-10 0c0 3 5 8 5 8z" fill="none" stroke="#fff" stroke-width="1.2"/><circle cx="6" cy="5" r="1.8" fill="none" stroke="#fff" stroke-width="1.2"/></svg>Brightlane Promo Works Group, Inc.<br>4120 Harbor View Road Suite 210<br>Bayport, CA 90000</li>
      <li><svg width="13" height="13" viewBox="0 0 13 13"><path d="M2 1l3 3-1.5 1.5a8 8 0 0 0 4 4L9 8l3 3-1.5 1.5C5 12 1 8 .5 2.5z" fill="none" stroke="#fff" stroke-width="1.1"/></svg>USA Office: 1-555-301-4420<br>International: 1-800-555-0142<br>Text Us: 1-555-303-8810</li>
      <li><svg width="13" height="10" viewBox="0 0 13 10"><rect x=".5" y=".5" width="12" height="9" fill="none" stroke="#fff"/><path d="M.5 .5l6 5 6-5" fill="none" stroke="#fff"/></svg>info@brightlanepromoworks.biz</li>
      <li><svg width="13" height="13" viewBox="0 0 13 13"><circle cx="6.5" cy="6.5" r="5.8" fill="none" stroke="#fff" stroke-width="1.1"/><path d="M6.5 3v3.5h2.5" fill="none" stroke="#fff" stroke-width="1.1"/></svg>24/7 Chat Support<br>24/7 Live Answering Service<br>24/7 Email Support<br>Live Phone &amp; SMS Support:<br>Monday - Friday 8am - 5pm PST<br>Sat/Sun/Holidays Closed</li>
    </ul>
  </div>

  <div class="f-col" style="left:797px;width:140px">
    <h3>QUICK LINKS</h3>
    <ul>
      <li>Home</li><li>The Incentives</li><li>Samples</li><li>Affiliate</li><li>Testimonials</li><li>Faq</li><li>Contact Us</li>
      <li>Redemption<br>Demo Videos</li><li>BPW Distribute<br>Certificate Demo<br>Videos</li>
    </ul>
  </div>

  <div class="f-col" style="left:952px;width:200px">
    <h3>OTHER LINKS</h3>
    <ul>
      <li>Hoteliers</li><li>BPW Certificates List</li><li>How To Use BPW Certificates</li><li>Social Incentive Campaign</li>
      <li>Pop Ups &amp; Sticky Bars</li><li>Whitepaper - Increase Sales</li><li>Whitepaper - Improve Sales<br>During Strange Times</li>
      <li>Whitepaper - Boost Website<br>Conversions</li>
    </ul>
  </div>
</footer>

</body>
</html>
```